FotoVELTA buisnesscard

Hey :) I need a modern buisnesscard for my company FotoVELTA
It most have:
Dagligleder og Fotograf: Henrik Torvald Bjelland

Mob: +4791642058
Epost: post@fotovelta.no
Adresse: Bakkestien22, 6017 Fjordvik

Facbook and instagram logo with text FotoVELTA

FotoVELTA logo

It Company

```html
<!DOCTYPE html>
<html lang="no">
<head>
<meta charset="utf-8">
<title>FotoVELTA – visittkort</title>
<link href="https://fonts.googleapis.com/css2?family=Arimo:wght@400;700&family=Zilla+Slab:wght@400;500&display=swap" rel="stylesheet">
<style>
  :root {
    --backdrop: #e9e9eb;
    --card-grey: #b9babc;
    --card-grey-light: #c4c5c7;
    --panel-white: #ffffff;
    --band-dark: #3a3a3b;
    --ink-dark: #333334;
    --logo-grey: #9c9d9f;
    --band-text: #eeeeee;
  }
  * { box-sizing: border-box; margin: 0; padding: 0; }
  html, body { width: 1200px; height: 1200px; overflow: hidden; }
  body {
    background: var(--backdrop);
    position: relative;
    font-family: "Arimo", Arial, sans-serif;
  }
  .card {
    position: absolute;
    top: 215px;
    width: 440px;
    height: 770px;
    background: linear-gradient(160deg, var(--card-grey-light), var(--card-grey));
    box-shadow: 0 10px 30px rgba(0,0,0,0.18);
    overflow: hidden;
  }
  .card--front { left: 120px; }
  .card--back { left: 640px; }

  /* Front side */
  .edge-tab {
    position: absolute;
    width: 42px;
    height: 104px;
    background: var(--band-dark);
  }
  .edge-tab--left { left: 0; top: 300px; }
  .edge-tab--right { right: 0; top: 390px; }
  .front-rotated {
    position: absolute;
    width: 770px;
    height: 440px;
    left: -165px;
    top: 165px;
    transform: rotate(-90deg);
    display: flex;
    flex-direction: column;
    align-items: center;
    justify-content: center;
    gap: 14px;
    color: var(--ink-dark);
  }
  .brand-square {
    width: 60px;
    height: 60px;
    background: var(--ink-dark);
  }
  .front-brand__name {
    font-weight: 700;
    font-size: 60px;
    line-height: 1;
    letter-spacing: -1px;
  }
  .social-row {
    display: flex;
    gap: 56px;
    font-size: 18px;
    font-weight: 700;
  }
  .social-handle { display: flex; align-items: center; gap: 8px; }
  .social-square { width: 16px; height: 16px; background: var(--ink-dark); }

  /* Back side */
  .back-panel {
    position: absolute;
    left: 24px;
    right: 24px;
    top: 24px;
    height: 565px;
    background: var(--panel-white);
  }
  .back-brand {
    position: absolute;
    left: 0; right: 0;
    top: 110px;
    display: flex;
    flex-direction: column;
    align-items: center;
    gap: 14px;
    color: var(--logo-grey);
  }
  .back-brand__square {
    width: 70px;
    height: 70px;
    background: var(--logo-grey);
  }
  .back-brand__name {
    font-weight: 700;
    font-size: 52px;
    line-height: 1;
    letter-spacing: -1px;
  }
  .title-band {
    position: absolute;
    left: 0; right: 0;
    top: 305px;
    height: 94px;
    background: var(--band-dark);
    color: var(--band-text);
    font-family: "Zilla Slab", Georgia, serif;
    text-align: center;
    padding-top: 12px;
  }
  .title-band__role { font-size: 24px; }
  .title-band__name { font-size: 31px; letter-spacing: 0.5px; }
  .contact-list {
    position: absolute;
    left: 60px;
    top: 420px;
    display: grid;
    grid-template-columns: 88px 1fr;
    row-gap: 6px;
    font-size: 18px;
    color: #111;
  }
  .contact-list dt { font-weight: 400; }
  .contact-list dd::before { content: ": "; }
  .website {
    position: absolute;
    left: 0; right: 0;
    bottom: 70px;
    text-align: center;
    font-family: "Zilla Slab", Georgia, serif;
    font-weight: 500;
    font-size: 22px;
    color: var(--ink-dark);
  }
</style>
</head>
<body>
  <section class="card card--front" aria-label="Forside av visittkort">
    <div class="edge-tab edge-tab--left"></div>
    <div class="edge-tab edge-tab--right"></div>
    <div class="front-rotated">
      <span class="brand-square"></span>
      <span class="front-brand__name">FotoVELTA</span>
      <div class="social-row">
        <span class="social-handle"><span class="social-square"></span>/FotoVELTA</span>
        <span class="social-handle"><span class="social-square"></span>/FotoVELTA</span>
      </div>
    </div>
  </section>

  <section class="card card--back" aria-label="Bakside av visittkort">
    <div class="back-panel">
      <div class="back-brand">
        <span class="back-brand__square"></span>
        <span class="back-brand__name">FotoVELTA</span>
      </div>
    </div>
    <div class="title-band">
      <div class="title-band__role">Dagligleder og Fotograf:</div>
      <div class="title-band__name">Henrik Torvald Bjelland</div>
    </div>
    <dl class="contact-list">
      <dt>Mob</dt><dd>+4791642058</dd>
      <dt>Epost</dt><dd>post@fotovelta.no</dd>
      <dt>Adresse</dt><dd>Bakkestien22, 6017<br>&nbsp;&nbsp;Fjordvik</dd>
    </dl>
    <div class="website">www.fotovelta.no</div>
  </section>
</body>
</html>
```